KVT Social Media Graphics (Square)

Use the following images and headlines to create 7 individual social media graphics (square size); You can mix and match the text that's there to create different social media graphics. Note: each graphic should have one of the pictures of the bottle on it and/or one of the images with a person on it (pics attached to the brief)

Target Market(s)

women and men who are overweight looking for fast, healthy weight loss

Industry/Entity Type

health and wellness

Colors
0054AA
0677BA
7BADD7
CADEEF
E8F1F8

Requirements
Must have
• Use color scheme that's complimentary to the blood sugar bottle
Nice to have
• the text provided in the WORD document

```html
<!DOCTYPE html>
<html lang="en">
<head>
<meta charset="utf-8">
<title>Weight Loss Supplement Social Graphics</title>
<link href="https://fonts.googleapis.com/css2?family=Poppins:wght@400;500;600&display=swap" rel="stylesheet">
<style>
  :root {
    --board: #d8d8d8;
    --white: #ffffff;
    --sky: #3ca1e6;
    --violet: #51408e;
    --violet-text: #4a3b8c;
    --periwinkle: #5b8fe0;
    --lavender: #dfe3f7;
    --steel: #4564b3;
    --ink: #222222;
    --photo-warm: #d9cfc4;
    --photo-cool: #b9bfd6;
    --photo-room: #d6d2cb;
  }
  * { box-sizing: border-box; margin: 0; padding: 0; }
  html, body { width: 1200px; height: 728px; overflow: hidden; background: var(--board); font-family: 'Poppins', sans-serif; }
  .board { position: relative; width: 1200px; height: 728px; }
  .tile { position: absolute; width: 230px; height: 230px; overflow: hidden; }
  .tile > svg.bg { position: absolute; inset: 0; }
  .abs { position: absolute; }
  .center { transform: translateX(-50%); text-align: center; }
  .photo { position: absolute; }

  .badge { position: absolute; width: 31px; height: 31px; border-radius: 50%; background: var(--white); color: var(--sky);
           transform: translate(-50%, -50%); display: flex; align-items: center; justify-content: center; }
  .badge svg { width: 17px; height: 17px; }
  .badge-label { position: absolute; width: 72px; transform: translateX(-50%); text-align: center; color: var(--white);
                 font-size: 4.6px; font-weight: 500; line-height: 1.25; }

  .line-icon { position: absolute; width: 17px; height: 17px; color: var(--white); transform: translate(-50%, -50%); }
  .item-text { position: absolute; color: var(--white); font-size: 6px; font-weight: 500; line-height: 1.2; transform: translateY(-50%); white-space: nowrap; }

  /* natural alternative */
  .tile-intro { left: 178px; top: 72px; background: var(--white); }
  .intro-head { left: 115px; top: 36px; width: 210px; font-size: 11.4px; font-weight: 600; line-height: 1.25; color: var(--violet-text); }
  .intro-head span { color: var(--periwinkle); }
  .benefit-list { left: 20px; top: 98px; list-style: none; font-size: 5.6px; font-weight: 500; color: var(--ink); }
  .benefit-list li { height: 12.9px; white-space: nowrap; }
  .benefit-list li::before { content: "»"; color: var(--periwinkle); margin-right: 4px; font-weight: 600; }
  .intro-halo { left: 152px; top: 76px; width: 124px; height: 122px; border-radius: 50%; background: var(--lavender); }

  /* secret to natural weight loss */
  .tile-secret { left: 463px; top: 72px; background: var(--violet); }
  .secret-head { left: 115px; top: 10px; width: 220px; color: var(--white); font-size: 7.6px; font-weight: 500; line-height: 1.8; }
  .product-card { left: 89px; top: 129px; width: 51px; height: 47px; border-radius: 3px; background: var(--white); }
  .product-card .photo { inset: 5px; border-radius: 2px; background: linear-gradient(180deg, #f2f3f7, #c9d1ea); }

  /* without side effects */
  .tile-nosides { left: 747px; top: 72px; background: var(--sky); }
  .nosides-head { left: 115px; top: 23px; width: 220px; color: var(--white); font-size: 7.6px; font-weight: 500; }
  .tile-nosides .item-text { font-size: 6.6px; }

  /* prescription-free */
  .tile-rxfree { left: 178px; top: 365px; background: var(--sky); }
  .rx-tag { left: 117px; top: 38px; width: 92px; height: 29px; border-radius: 3px; background: rgba(255,255,255,0.82);
            font-size: 8.6px; font-weight: 600; line-height: 1.2; text-align: center; padding-top: 2px; color: var(--violet-text); }
  .rx-tag span { color: var(--sky); }

  /* boost glp-1 */
  .tile-boost { left: 463px; top: 365px; background: var(--steel); }
  .boost-head { left: 171px; top: 40px; width: 120px; font-size: 10.6px; font-weight: 600; line-height: 1.22; color: var(--violet-text); }
  .boost-head span { color: var(--sky); }

  /* clinically studied */
  .tile-clinical { left: 747px; top: 365px; background: var(--sky); }
  .clinical-head { left: 115px; top: 19px; width: 220px; font-size: 11px; font-weight: 600; line-height: 1.2; color: var(--violet-text); }
  .clinical-halo { left: 7px; top: 85px; width: 98px; height: 98px; border-radius: 50%; background: radial-gradient(circle at 50% 45%, #ffffff, #e4e7f1); }
</style>
</head>
<body>
<svg width="0" height="0" style="position:absolute" aria-hidden="true">
  <defs>
    <symbol id="i-flame" viewBox="0 0 24 24"><g fill="none" stroke="currentColor" stroke-width="1.6" stroke-linejoin="round" stroke-linecap="round"><path d="M12 2.5c1 4 6.5 6 6.5 11.5a6.5 6.5 0 0 1-13 0c0-3 2-4.5 2.2-6.8 1.8 1 3 3 3 3 .2-3.2 0-5.5 1.3-7.7z"/><path d="M12.6 11.5l-2.4 3.6h3l-1.6 3.4"/></g></symbol>
    <symbol id="i-dna" viewBox="0 0 24 24"><g fill="none" stroke="currentColor" stroke-width="1.6" stroke-linecap="round"><path d="M7 2c0 6 10 8 10 14s-4 5-4 6"/><path d="M17 2c0 6-10 8-10 14s4 5 4 6"/><path d="M8.5 5h7M10 8.5h4M10 15.5h4M8.5 19h7"/></g></symbol>
    <symbol id="i-person" viewBox="0 0 24 24"><g fill="none" stroke="currentColor" stroke-width="1.6" stroke-linecap="round"><circle cx="9" cy="7" r="3.5"/><path d="M2.5 21c0-4.5 3-7.5 6.5-7.5s6.5 3 6.5 7.5z"/><rect x="15.5" y="5" width="6.5" height="5" rx="1"/></g></symbol>
    <symbol id="i-watch" viewBox="0 0 24 24"><g fill="none" stroke="currentColor" stroke-width="1.6" stroke-linecap="round"><circle cx="12" cy="13.5" r="8"/><path d="M10 3h4M12 3v2.5M12 13.5l3-3M18.5 6.5l1.5-1.5"/></g></symbol>
    <symbol id="i-drop" viewBox="0 0 24 24"><g fill="none" stroke="currentColor" stroke-width="1.6" stroke-linecap="round" stroke-linejoin="round"><path d="M12 2.5S5.5 10 5.5 14.5a6.5 6.5 0 0 0 13 0C18.5 10 12 2.5 12 2.5z"/><path d="M12 12v5M9.5 14.5h5"/></g></symbol>
  </defs>
</svg>

<main class="board">

  <section class="tile tile-intro">
    <h2 class="abs center intro-head">Have You Heard About the Natural <span>Alternative to Weight Loss Drugs?</span></h2>
    <ul class="abs benefit-list">
      <li>Increase GLP-1 Levels*</li>
      <li>Support Fat Loss*</li>
      <li>Reduce Cravings for Sugar and Carbs*</li>
      <li>Feel Full Faster &amp; Stay Full Longer*</li>
      <li>Support Healthy Blood Sugar Levels*</li>
    </ul>
    <div class="abs intro-halo"></div>
    <div class="photo" role="img" aria-label="Supplement bottle with white cap and blue label" style="left:180px;top:96px;width:39px;height:82px;border-radius:5px;background:linear-gradient(180deg,#f4f5f8 0%,#e8ebf4 55%,#2f4fa8 100%);"></div>
  </section>

  <section class="tile tile-secret">
    <svg class="bg" viewBox="0 0 230 230"><path d="M0 56 Q115 28 230 56 L230 172 Q115 130 0 172 Z" fill="var(--sky)"/></svg>
    <h2 class="abs center secret-head">Have You Heard About<br>The Secret to Natural Weight Loss?</h2>
    <div class="badge" style="left:113px;top:76px"><svg><use href="#i-flame"/></svg></div>
    <p class="badge-label" style="left:113px;top:97px">Support Fat Loss*</p>
    <div class="badge" style="left:45px;top:115px"><svg><use href="#i-dna"/></svg></div>
    <p class="badge-label" style="left:45px;top:136px">Increase GLP-1<br>Levels*</p>
    <div class="badge" style="left:179px;top:115px"><svg><use href="#i-person"/></svg></div>
    <p class="badge-label" style="left:179px;top:136px">Reduce Cravings for<br>Sugar and Carbs*</p>
    <div class="badge" style="left:54px;top:187px"><svg><use href="#i-watch"/></svg></div>
    <p class="badge-label" style="left:59px;top:207px">Feel Full Faster &amp; Stay<br>Full Longer*</p>
    <div class="badge" style="left:170px;top:187px"><svg><use href="#i-drop"/></svg></div>
    <p class="badge-label" style="left:170px;top:207px">Support Healthy<br>Blood Sugar Levels*</p>
    <div class="abs product-card"><div class="photo" role="img" aria-label="Three supplement bottles side by side"></div></div>
  </section>

  <section class="tile tile-nosides">
    <svg class="bg" viewBox="0 0 230 230"><path d="M0 120 C50 150 170 135 230 100 L230 230 L0 230 Z" fill="var(--violet)"/></svg>
    <h2 class="abs center nosides-head">Lose Weight, Without the Side Effects*</h2>
    <svg class="line-icon" style="left:22px;top:70px"><use href="#i-flame"/></svg>
    <p class="item-text" style="left:33px;top:70px">Support Fat Loss*</p>
    <svg class="line-icon" style="left:20px;top:103px"><use href="#i-drop"/></svg>
    <p class="item-text" style="left:31px;top:102px">Reduce Cravings<br>for Sugar and Carbs*</p>
    <svg class="line-icon" style="left:23px;top:148px"><use href="#i-watch"/></svg>
    <p class="item-text" style="left:36px;top:147px">Feel Full Faster<br>&amp; Stay Full Longer</p>
    <svg class="line-icon" style="left:21px;top:191px"><use href="#i-person"/></svg>
    <p class="item-text" style="left:37px;top:190px">Support Healthy<br>Blood Sugar Levels*</p>
    <div class="photo" role="img" aria-label="Woman in a pink blazer holding a supplement bottle beside a glass of water" style="left:118px;top:75px;width:99px;height:109px;border-radius:3px;background:linear-gradient(160deg,#8fa27a 0%,#5d6a58 45%,#c63a95 100%);"></div>
  </section>

  <section class="tile tile-rxfree">
    <div class="photo" role="img" aria-label="Smiling woman holding out the waistband of oversized jeans in a bright room" style="left:0;top:0;width:230px;height:150px;background:linear-gradient(120deg,var(--photo-room) 0%,#c9b9a6 45%,#8fb0d3 70%,var(--photo-warm) 100%);"></div>
    <svg class="bg" viewBox="0 0 230 230">
      <path d="M0 126 C50 92 95 98 140 128 C175 150 205 135 230 108" fill="none" stroke="var(--violet)" stroke-width="4"/>
      <path d="M0 131 C50 97 95 103 140 133 C175 155 205 140 230 113 L230 230 L0 230 Z" fill="var(--sky)"/>
    </svg>
    <div class="abs rx-tag"><span>Prescription-Free</span><br>Weight Loss*</div>
    <svg class="line-icon" style="left:35px;top:162px"><use href="#i-watch"/></svg>
    <p class="item-text" style="left:49px;top:161px">Feel Full Faster<br>&amp; Stay Full Longer</p>
    <svg class="line-icon" style="left:137px;top:163px"><use href="#i-person"/></svg>
    <p class="item-text" style="left:150px;top:163px">Support Healthy<br>Blood Sugar Levels*</p>
    <svg class="line-icon" style="left:35px;top:207px"><use href="#i-drop"/></svg>
    <p class="item-text" style="left:47px;top:206px">Reduce Cravings<br>for Sugar and Carbs*</p>
    <svg class="line-icon" style="left:138px;top:207px"><use href="#i-flame"/></svg>
    <p class="item-text" style="left:150px;top:210px">Support Fat Loss*</p>
  </section>

  <section class="tile tile-boost">
    <div class="photo" role="img" aria-label="Supplement bottle between two lemon halves on a marble surface" style="left:0;top:0;width:230px;height:140px;background:linear-gradient(100deg,#e4e6ee 0%,var(--photo-cool) 55%,#aab3cf 100%);"></div>
    <h2 class="abs center boost-head"><span>Boost GLP-1<br>Levels</span> And Support<br>Fat Loss*</h2>
    <svg class="line-icon" style="left:33px;top:162px"><use href="#i-watch"/></svg>
    <p class="item-text" style="left:46px;top:162px">Feel Full Faster<br>&amp; Stay Full Longer</p>
    <svg class="line-icon" style="left:134px;top:164px"><use href="#i-person"/></svg>
    <p class="item-text" style="left:148px;top:164px">Support Healthy<br>Blood Sugar Levels*</p>
    <svg class="line-icon" style="left:32px;top:208px"><use href="#i-drop"/></svg>
    <p class="item-text" style="left:45px;top:207px">Reduce Cravings<br>for Sugar and Carbs*</p>
    <svg class="line-icon" style="left:135px;top:208px"><use href="#i-flame"/></svg>
    <p class="item-text" style="left:148px;top:211px">Support Fat Loss*</p>
  </section>

  <section class="tile tile-clinical">
    <h2 class="abs center clinical-head">Clinically-Studied Ingredients<br>for Natural Weight Loss*</h2>
    <div class="abs clinical-halo" role="img" aria-label="Supplement bottle lying on its side with capsules spilling out"></div>
    <div class="badge" style="left:131px;top:78px"><svg><use href="#i-flame"/></svg></div>
    <p class="badge-label" style="left:131px;top:99px">Support Fat Loss*</p>
    <div class="badge" style="left:192px;top:97px"><svg><use href="#i-drop"/></svg></div>
    <p class="badge-label" style="left:192px;top:117px">Support Healthy<br>Blood Sugar Levels*</p>
    <div class="badge" style="left:139px;top:130px"><svg><use href="#i-dna"/></svg></div>
    <p class="badge-label" style="left:139px;top:151px">Increase GLP-1<br>Levels*</p>
    <div class="badge" style="left:194px;top:157px"><svg><use href="#i-person"/></svg></div>
    <p class="badge-label" style="left:194px;top:178px">Reduce Cravings for<br>Sugar and Carbs*</p>
    <div class="badge" style="left:127px;top:188px"><svg><use href="#i-watch"/></svg></div>
    <p class="badge-label" style="left:131px;top:209px">Feel Full Faster &amp; Stay<br>Full Longer*</p>
  </section>

</main>
</body>
</html>
```